Brivomark Business Card

Brivomark is a young and energetic software development consultancy. We spend our time on the road working with clients on their sites an meeting new potential customers and employees!

We need a sharp, vibrant and memorable business card that will inspires those that receive it to look after it as it oozes quality and is a nice thing in its own right.

We like bold colours and distinctive design. So show us what you can do.

In terms of information on the card, it would be good to see:

* Our logo (Obviously :) )
* Employee name
* Email
* Website address
* Mobile number
* Full company name (Brivomark ltd)
* Registered company number
* Registered company address

Industry/Entity Type

Software

Requirements
Nice to have
• We are thinking that having a QR Code on the business card could be a good way of adding active marketing. It would be good to see if you are able to merge the kind of element in to your designs!

Maybe something special could be achieved using a visual QR Code like those produced at http://www.quenprint-example.com/ ? You have our media so feel free to have a play.

```html
<!DOCTYPE html>
<html lang="en">
<head>
<meta charset="utf-8">
<title>Brivomark Business Card</title>
<link href="https://fonts.googleapis.com/css2?family=Bebas+Neue&family=Open+Sans:ital,wght@1,400&display=swap" rel="stylesheet">
<style>
  :root {
    --page-bg: #e6e6e6;
    --card-dark: #2b2b2b;
    --card-darker: #161616;
    --brand-red: #b8202c;
    --brand-red-deep: #6e141b;
    --ink-white: #f4f4f4;
    --ink-dark: #2e2e2e;
    --logo-ink: #4a0c12;
  }
  html, body {
    margin: 0;
    width: 1200px;
    height: 900px;
    overflow: hidden;
    background: var(--page-bg);
  }
  .stage {
    position: relative;
    width: 1200px;
    height: 900px;
  }
  .card {
    position: absolute;
    top: 280px;
    width: 560px;
    height: 340px;
    overflow: hidden;
    box-shadow: 0 10px 28px rgba(0,0,0,.3);
  }
  .card--front {
    left: 30px;
    background: radial-gradient(ellipse at 55% 40%, #3a3a3a 0%, var(--card-dark) 45%, var(--card-darker) 100%);
  }
  .card--back {
    left: 610px;
    background: radial-gradient(ellipse at 40% 45%, var(--brand-red) 0%, #8e1a23 50%, var(--brand-red-deep) 100%);
  }
  .puzzle-art {
    position: absolute;
  }
  .puzzle-art--red {
    left: -20px; top: -20px;
    width: 170px; height: 200px;
    background: radial-gradient(ellipse at 40% 40%, #c0222e 0%, #8a1820 70%, rgba(138,24,32,0) 100%);
  }
  .puzzle-art--dark {
    right: -30px; bottom: -30px;
    width: 170px; height: 230px;
    background: radial-gradient(ellipse at 55% 55%, #2a2a2a 0%, #3a1a1c 65%, rgba(58,26,28,0) 100%);
  }
  .holder-name {
    position: absolute;
    left: 80px; top: 92px;
    width: 400px;
    margin: 0;
    text-align: center;
    white-space: nowrap;
    font: 54px/1 "Bebas Neue", sans-serif;
    font-weight: 400;
    color: var(--ink-white);
    letter-spacing: 1px;
  }
  .holder-role {
    position: absolute;
    left: 80px; top: 150px;
    width: 400px;
    margin: 0;
    text-align: center;
    white-space: nowrap;
    font: 25px/1 "Bebas Neue", sans-serif;
    color: var(--ink-white);
    letter-spacing: 1px;
  }
  .rule {
    position: absolute;
    left: 90px; top: 186px;
    width: 380px; height: 1px;
    background: linear-gradient(90deg, rgba(255,255,255,0), rgba(255,255,255,.35), rgba(255,255,255,0));
  }
  .brand-tab {
    position: absolute;
    left: 150px; top: 194px;
    width: 260px; height: 92px;
  }
  .brand-tab__name {
    position: absolute;
    left: 0; top: 20px;
    width: 260px;
    text-align: center;
    white-space: nowrap;
    font: 42px/1 "Bebas Neue", sans-serif;
    color: var(--logo-ink);
    letter-spacing: 2px;
  }
  .brand-watermark {
    position: absolute;
    left: 20px; top: 4px;
    margin: 0;
    white-space: nowrap;
    font: 110px/1 "Bebas Neue", sans-serif;
    color: rgba(60,10,14,.35);
    letter-spacing: 4px;
  }
  .company-name {
    position: absolute;
    left: 0; top: 68px;
    width: 560px;
    margin: 0;
    text-align: center;
    white-space: nowrap;
    font: 54px/1 "Bebas Neue", sans-serif;
    font-weight: 400;
    color: var(--ink-white);
    letter-spacing: 1px;
  }
  .company-reg {
    position: absolute;
    left: 0; top: 134px;
    width: 560px;
    margin: 0;
    text-align: center;
    white-space: nowrap;
    font: 20px/1.3 "Bebas Neue", sans-serif;
    color: var(--ink-white);
    letter-spacing: .5px;
  }
  .contact-panel {
    position: absolute;
    left: 150px; top: 196px;
    width: 260px; height: 96px;
  }
  .contact-list {
    position: absolute;
    left: 16px; top: 10px;
    margin: 0; padding: 0;
    list-style: none;
    white-space: nowrap;
    font: italic 17px/1.25 "Open Sans", sans-serif;
    color: var(--ink-dark);
  }
</style>
</head>
<body>
<main class="stage">
  <section class="card card--front" aria-label="Business card front">
    <div class="puzzle-art puzzle-art--red" role="img" aria-label="Red puzzle pieces illustration"></div>
    <h1 class="holder-name">Owen Hartley</h1>
    <p class="holder-role">Sales Manager</p>
    <div class="rule"></div>
    <div class="brand-tab">
      <svg width="260" height="92" viewBox="0 0 260 92" aria-hidden="true">
        <defs>
          <linearGradient id="tabRed" x1="0" y1="0" x2="0" y2="1">
            <stop offset="0" stop-color="#d8283a"/>
            <stop offset="1" stop-color="#a81a26"/>
          </linearGradient>
        </defs>
        <path d="M0 0 H260 V68 Q260 76 252 76 H8 Q0 76 0 68 Z" fill="url(#tabRed)"/>
        <path d="M40 92 L130 80 L220 92 Z" fill="#6a6a6a"/>
      </svg>
      <span class="brand-tab__name">Brivomark</span>
    </div>
  </section>

  <section class="card card--back" aria-label="Business card back">
    <p class="brand-watermark" aria-hidden="true">Brivomark</p>
    <div class="puzzle-art puzzle-art--dark" role="img" aria-label="Dark puzzle pieces illustration"></div>
    <h2 class="company-name">Brivomark Ltd</h2>
    <p class="company-reg">Registered company number 0478812KM50931<br>48 Larkfield Road Easton, NY 10234</p>
    <div class="contact-panel">
      <svg width="260" height="96" viewBox="0 0 260 96" aria-hidden="true">
        <defs>
          <linearGradient id="panelGrey" x1="0" y1="0" x2="0" y2="1">
            <stop offset="0" stop-color="#bdbdbd"/>
            <stop offset="1" stop-color="#959595"/>
          </linearGradient>
        </defs>
        <path d="M0 0 H260 V74 Q260 82 252 82 H8 Q0 82 0 74 Z" fill="url(#panelGrey)"/>
        <path d="M40 96 L130 84 L220 96 Z" fill="#5a1218"/>
      </svg>
      <ul class="contact-list">
        <li>mobile. 001 555 010 234</li>
        <li>email. info@brivomark.com</li>
        <li>web. www.brivomark.com</li>
      </ul>
    </div>
  </section>
</main>
</body>
</html>
```